Healthcare Recruitment Agency Brochure

We need our current Brochure updated as its old and dated. The brochure will be for our current and potential Clients and should provide all the necessary information regarding our services, but in a well presented, easy reading format which echoes our company Brand. The company supplies Healthcare establishments with trained healthcare Staff which can be in a variety of settings.
UPDATE: Following the submission of many designs we would like to amend the information/content to be included in the brochure and have uploaded additional information. We would like an 8 page booklet with the various sections spread out so as not to look to 'wordy' page 1 Front cover, 2 About Us, 3 Our Service, 4 Our promise, 5 Our Staff, 6 Our Ethos, 7 What Our Clients Say/Testimonials, 8 Contact Us/Back page. Please if using pictures (which is welcomed) steer away from the surgical/doctor type. We mainly provide care to the Elderly within Nursing and Residential Homes and Support Environments. Thanks
Updates

Target Market(s)

Healthcare clientell

Industry/Entity Type

Healthcare

Requirements
Must have
• Pictures, animation, easy reading, informative, tie in with website theme www.carewellstaffline.example
Nice to have
• open to ideas
Should not have
• very long text paragraphs

```html
<!DOCTYPE html>
<html lang="en">
<head>
<meta charset="utf-8">
<title>CareWell Staffline Brochure Covers</title>
<link href="https://fonts.googleapis.com/css2?family=Montserrat:wght@400;500;600;700&family=Oswald:wght@500;600&display=swap" rel="stylesheet">
<style>
  :root {
    --canvas: #3a3a3a;
    --paper: #eef7f8;
    --paper-edge: #e3f0f2;
    --brand-blue: #1f5aa6;
    --brand-teal: #1fa58a;
    --ink: #2b2f36;
    --white: #ffffff;
    --photo-warm-a: #d9c6a8;
    --photo-warm-b: #a88f7a;
    --photo-green-a: #6f8f4a;
    --photo-green-b: #9fb6d2;
  }
  * { margin: 0; padding: 0; box-sizing: border-box; }
  html, body { width: 1200px; height: 824px; overflow: hidden; background: var(--canvas); }
  body { font-family: "Montserrat", Arial, sans-serif; color: var(--ink); }
  .spread { position: absolute; left: 60px; top: 30px; width: 1080px; height: 764px; display: flex; }
  .page { position: relative; width: 540px; height: 764px; background: linear-gradient(160deg, var(--paper) 0%, var(--white) 100%); overflow: hidden; }
  .page--back { border-right: 1px solid var(--paper-edge); }
  .bottom-rule { position: absolute; left: 0; right: 0; bottom: 0; height: 6px; background: var(--brand-teal); }

  .photo-frame { position: absolute; border: 4px solid var(--brand-blue); border-radius: 28px; }
  .photo-frame--garden { left: 50px; top: 60px; width: 330px; height: 320px; background: linear-gradient(135deg, var(--photo-green-a), var(--photo-green-b)); }
  .photo-frame--home { left: 40px; top: 130px; width: 440px; height: 370px; background: linear-gradient(135deg, var(--photo-warm-a), var(--photo-warm-b)); }
  .accent-rule { position: absolute; height: 5px; background: var(--brand-teal); }
  .accent-rule--back { left: 0; right: 0; top: 400px; }
  .accent-rule--front { left: 0; right: 0; top: 520px; }

  .section-label { position: absolute; display: flex; font-family: "Oswald", "Arial Narrow", sans-serif; font-size: 22px; letter-spacing: 1px; line-height: 1; }
  .section-label span { padding: 6px 10px; color: var(--white); }
  .section-label .label-light { background: var(--brand-teal); font-weight: 500; }
  .section-label .label-bold { background: var(--brand-blue); font-weight: 600; }

  .branch-list { position: absolute; left: 64px; top: 484px; width: 300px; list-style: none; }
  .branch { margin-bottom: 6px; }
  .branch-town { font-size: 11.5px; font-weight: 700; color: var(--brand-blue); text-transform: uppercase; }
  .branch-line { display: flex; align-items: center; gap: 6px; font-size: 11px; line-height: 15px; }
  .branch-line svg { width: 11px; height: 11px; flex: none; }
  .contact-lines { position: absolute; left: 64px; top: 702px; font-size: 11px; line-height: 19px; }

  .brand-name { font-family: "Montserrat", Arial, sans-serif; font-weight: 600; color: var(--brand-blue); display: flex; align-items: center; gap: 8px; }
  .brand-dot { border-radius: 50%; background: var(--brand-teal); flex: none; }
  .brand-name--small { position: absolute; left: 360px; top: 580px; font-size: 15px; }
  .brand-name--small .brand-dot { width: 9px; height: 9px; }
  .brand-name--large { position: absolute; left: 0; right: 0; top: 50px; justify-content: center; font-size: 34px; }
  .brand-name--large .brand-dot { width: 16px; height: 16px; }

  .social-row { position: absolute; left: 392px; top: 612px; display: flex; gap: 12px; list-style: none; }
  .social-row li { width: 20px; height: 20px; border-radius: 50%; background: var(--brand-teal); }

  .solutions-copy { position: absolute; left: 290px; top: 588px; width: 220px; font-size: 12px; line-height: 16px; }
  .solutions-copy strong { color: var(--brand-blue); font-weight: 700; }
  .web-pill { position: absolute; left: 60px; right: 40px; top: 680px; height: 34px; border-radius: 17px; background: var(--brand-blue); color: var(--white); font-size: 13px; font-weight: 600; letter-spacing: 3px; display: flex; align-items: center; justify-content: center; }
</style>
</head>
<body>
<main class="spread">

  <section class="page page--back" aria-label="Back cover">
    <div class="accent-rule accent-rule--back"></div>
    <div class="photo-frame photo-frame--garden" role="img" aria-label="Photo: smiling carer pushing an elderly man in a wheelchair through a garden"></div>

    <div class="section-label" style="left:64px; top:440px;">
      <span class="label-light">OUR</span><span class="label-bold">BRANCHES</span>
    </div>

    <ul class="branch-list">
      <li class="branch">
        <div class="branch-town">Maidstone | Kent</div>
        <div class="branch-line"><svg viewBox="0 0 12 12"><path d="M6 11 C3 7 2 5.5 2 4.2 A4 4 0 0 1 10 4.2 C10 5.5 9 7 6 11 Z" fill="var(--brand-teal)"/></svg>14 Orchard Row, Maidstone, Kent, ME1 0AA</div>
        <div class="branch-line"><svg viewBox="0 0 12 12"><circle cx="6" cy="6" r="5" fill="none" stroke="var(--brand-teal)" stroke-width="1.4"/><path d="M4 3.5 L5 5 L4.5 5.8 Q5.5 7.3 6.2 7.5 L7 7 L8.5 8" fill="none" stroke="var(--brand-teal)" stroke-width="1.2"/></svg>01632 960 101</div>
      </li>
      <li class="branch">
        <div class="branch-town">Tonbridge | Kent</div>
        <div class="branch-line"><svg viewBox="0 0 12 12"><path d="M6 11 C3 7 2 5.5 2 4.2 A4 4 0 0 1 10 4.2 C10 5.5 9 7 6 11 Z" fill="var(--brand-teal)"/></svg>38 Mill Lane, Tonbridge, TN1 0AB</div>
        <div class="branch-line"><svg viewBox="0 0 12 12"><circle cx="6" cy="6" r="5" fill="none" stroke="var(--brand-teal)" stroke-width="1.4"/><path d="M4 3.5 L5 5 L4.5 5.8 Q5.5 7.3 6.2 7.5 L7 7 L8.5 8" fill="none" stroke="var(--brand-teal)" stroke-width="1.2"/></svg>01632 960 202</div>
      </li>
      <li class="branch">
        <div class="branch-town">Dartford | Kent</div>
        <div class="branch-line"><svg viewBox="0 0 12 12"><path d="M6 11 C3 7 2 5.5 2 4.2 A4 4 0 0 1 10 4.2 C10 5.5 9 7 6 11 Z" fill="var(--brand-teal)"/></svg>5 Linden Court, Elm Hill, Dartford, Kent, DA1 0AC</div>
        <div class="branch-line"><svg viewBox="0 0 12 12"><circle cx="6" cy="6" r="5" fill="none" stroke="var(--brand-teal)" stroke-width="1.4"/><path d="M4 3.5 L5 5 L4.5 5.8 Q5.5 7.3 6.2 7.5 L7 7 L8.5 8" fill="none" stroke="var(--brand-teal)" stroke-width="1.2"/></svg>01632 960 303</div>
      </li>
      <li class="branch">
        <div class="branch-town">Ashford | Kent</div>
        <div class="branch-line"><svg viewBox="0 0 12 12"><path d="M6 11 C3 7 2 5.5 2 4.2 A4 4 0 0 1 10 4.2 C10 5.5 9 7 6 11 Z" fill="var(--brand-teal)"/></svg>17b Market Street, Ashford, Kent, TN23 0AD</div>
        <div class="branch-line"><svg viewBox="0 0 12 12"><circle cx="6" cy="6" r="5" fill="none" stroke="var(--brand-teal)" stroke-width="1.4"/><path d="M4 3.5 L5 5 L4.5 5.8 Q5.5 7.3 6.2 7.5 L7 7 L8.5 8" fill="none" stroke="var(--brand-teal)" stroke-width="1.2"/></svg>01632 960 404</div>
      </li>
    </ul>

    <div class="contact-lines">
      <div>✉&nbsp; info@carewellstaffline.example</div>
      <div>◍&nbsp; www.carewellstaffline.example</div>
    </div>

    <div class="brand-name brand-name--small"><span class="brand-dot"></span>CareWell Staffline</div>
    <ul class="social-row" aria-label="Social media profiles">
      <li role="img" aria-label="Social media profile link"></li>
      <li role="img" aria-label="Social media profile link"></li>
      <li role="img" aria-label="Social media profile link"></li>
    </ul>
    <div class="bottom-rule"></div>
  </section>

  <section class="page page--front" aria-label="Front cover">
    <div class="brand-name brand-name--large"><span class="brand-dot"></span>CareWell Staffline</div>

    <div class="accent-rule accent-rule--front"></div>
    <div class="photo-frame photo-frame--home" role="img" aria-label="Photo: carer in a white uniform walking arm in arm with a smiling elderly woman indoors"></div>

    <div class="section-label" style="left:290px; top:548px;">
      <span class="label-light">SUPERIOR</span><span class="label-bold">SOLUTIONS</span>
    </div>
    <p class="solutions-copy">We supply <strong>qualified, experienced</strong> local staff, dedicated to delivering <strong>excellent services.</strong></p>

    <div class="web-pill">www.carewellstaffline.example</div>
    <div class="bottom-rule"></div>
  </section>

</main>
</body>
</html>
```